Book cover for a very impressive real-life healing story from a stage IV deadly disease

I need a book cover design for the French translation of the US book http://www.pagevendo.com/Tims-Journey-Fever-Outlasted-Illness/dp/0845512097/ref=sr_1_4?s=books&ie=UTF8&qid=1455100794&sr=1-4&keywords=kit+marsh
.
I do not want the word AIDS on the French cover, as the story of this book applies to any disease.

The french title will be something like :
Un nouveau matin !
Condamné par la médecine, il guérit grâce au jeûne, la détoxination, et l’amour.

which means something like
A new morning!
Subtitle : Given up by official medecine, he managed to heal with fasting, detox and love.

Many thanks !

Target Market(s)

Anybody interested in natural health

Requirements
Must have
• Nothing special
Nice to have
• Nothing special
Should not have
• Nothing special

```html
<!DOCTYPE html>
<html lang="fr">
<head>
<meta charset="utf-8">
<title>Un nouveau matin ! — Kit Marsh</title>
<link href="https://fonts.googleapis.com/css2?family=League+Gothic&family=Zilla+Slab:wght@600;700&display=swap" rel="stylesheet">
<style>
  :root {
    --leaf-dark: #2f7a1f;
    --leaf-mid: #4f9e2c;
    --leaf-light: #8fcf4f;
    --disc: #62a52e;
    --side-disc: #a3b33a;
    --ink-light: #ffffff;
  }
  html, body {
    margin: 0;
    padding: 0;
    overflow: hidden;
    background: #ffffff;
  }
  .cover {
    position: relative;
    width: 801px;
    height: 1200px;
    overflow: hidden;
  }
  .cover__leaf {
    position: absolute;
    inset: 0;
    background:
      radial-gradient(ellipse 70% 55% at 30% 25%, var(--leaf-light) 0%, transparent 70%),
      radial-gradient(ellipse 60% 50% at 80% 85%, #7cc244 0%, transparent 70%),
      linear-gradient(135deg, var(--leaf-mid) 0%, var(--leaf-dark) 55%, #3f8f25 100%);
  }
  .cover__disc {
    position: absolute;
    left: 228px;
    top: 240px;
    width: 345px;
    height: 345px;
    border-radius: 50%;
    background: var(--disc);
  }
  .cover__side-disc {
    position: absolute;
    top: 362px;
    width: 100px;
    height: 100px;
    border-radius: 50%;
    background: var(--side-disc);
  }
  .cover__side-disc--left { left: -50px; }
  .cover__side-disc--right { right: -50px; }
  .cover__title {
    position: absolute;
    inset: 0;
    width: 801px;
    height: 1200px;
  }
  .cover__title text {
    font-family: "League Gothic", "Oswald", sans-serif;
    fill: var(--ink-light);
    text-transform: uppercase;
  }
  .cover__subtitle {
    position: absolute;
    left: 228px;
    top: 360px;
    width: 345px;
    margin: 0;
    text-align: center;
    font-family: "Zilla Slab", Georgia, serif;
    font-weight: 700;
    font-size: 25px;
    line-height: 1.2;
    color: var(--ink-light);
  }
  .cover__author {
    position: absolute;
    left: 0;
    right: 0;
    top: 1030px;
    margin: 0;
    text-align: center;
    font-family: "Zilla Slab", Georgia, serif;
    font-weight: 700;
    font-size: 34px;
    color: var(--ink-light);
  }
</style>
</head>
<body>
  <main class="cover">
    <div class="cover__leaf" role="img" aria-label="Gros plan d'une feuille verte rétroéclairée aux nervures apparentes"></div>
    <div class="cover__side-disc cover__side-disc--left"></div>
    <div class="cover__side-disc cover__side-disc--right"></div>
    <div class="cover__disc"></div>

    <svg class="cover__title" viewBox="0 0 801 1200" aria-label="Un nouveau matin !">
      <text x="400" y="332" text-anchor="middle" font-size="330" textLength="720" lengthAdjust="spacingAndGlyphs">Un nouveau</text>
      <text x="400" y="948" text-anchor="middle" font-size="540" textLength="720" lengthAdjust="spacingAndGlyphs">Matin !</text>
    </svg>

    <p class="cover__subtitle">Condamné par la médecine,<br>il guérit grâce au jeûne,<br>la détoxination, et l’amour</p>

    <p class="cover__author">Kit Marsh</p>
  </main>
</body>
</html>
```